Hi,

I would like to have a invitation made for a party. exactly like the picture in the link below.

http://pinboardia.example/pin/730215948361027459/

However, Please change the colors into fun/ girly feeling. font can be different and size of the card should be the same

Name of the girl: RINA
What: Bachelorette Party
Where:TOLO Boat
Dubai Coral Quay Sailing Club
When:7th of February 2013

No RSVP required. (so no need to put it)

```html
<!DOCTYPE html>
<html lang="en">
<head>
<meta charset="utf-8">
<title>Rina's Bachelorette Party Invitation</title>
<link rel="stylesheet" href="https://fonts.googleapis.com/css2?family=Cinzel:wght@400;500&display=swap">
<style>
  :root {
    --accent: #d93d7a;
    --accent-soft: #f3a6c6;
    --pattern-top: #fde9f1;
    --pattern-bottom: #f9d9e7;
    --card: #ffffff;
    --divider: #f2dbe5;
    --figure-tone: #f6cfe0;
  }
  html, body {
    margin: 0;
    padding: 0;
    overflow: hidden;
    background: var(--card);
  }
  .invitation {
    position: relative;
    width: 1200px;
    height: 560px;
    overflow: hidden;
    background: var(--card);
    font-family: "Cinzel", serif;
    color: var(--accent);
  }
  .leaf-band {
    position: absolute;
    left: 0;
    width: 1200px;
    background: linear-gradient(180deg, var(--pattern-top) 0%, var(--pattern-bottom) 100%);
  }
  .leaf-band--top { top: 0; height: 108px; }
  .leaf-band--bottom { top: 453px; height: 107px; }
  .title-art {
    position: absolute;
    left: 0;
    top: 0;
    width: 1200px;
    height: 560px;
  }
  .title-art text {
    font-family: "Cinzel", serif;
    fill: var(--accent);
  }
  .card-band { fill: var(--card); }
  .scallop-line {
    fill: none;
    stroke: var(--accent-soft);
    stroke-width: 1.4;
  }
  .panel-divider {
    stroke: var(--divider);
    stroke-width: 1.5;
  }
  .figure-slot { fill: var(--figure-tone); }
  .details {
    position: absolute;
    left: 800px;
    top: 186px;
    width: 400px;
    text-align: center;
    margin: 0;
  }
  .details dt {
    font-size: 14px;
    line-height: 16px;
    margin: 0;
  }
  .details dd {
    font-size: 18px;
    line-height: 22px;
    margin: 1px 0 10px;
  }
</style>
</head>
<body>
<main class="invitation">
  <div class="leaf-band leaf-band--top" role="img" aria-label="Soft pink pattern of outlined leaves"></div>
  <div class="leaf-band leaf-band--bottom" role="img" aria-label="Soft pink pattern of outlined leaves"></div>

  <svg class="title-art" viewBox="0 0 1200 560" width="1200" height="560" aria-labelledby="headline">
    <defs>
      <pattern id="scallop" width="12" height="8" patternUnits="userSpaceOnUse">
        <path class="scallop-line" d="M0 4 Q3 0 6 4 T12 4"/>
      </pattern>
    </defs>

    <rect class="card-band" x="0" y="108" width="1200" height="345"/>
    <rect class="scallop-edge" x="0" y="104" width="1200" height="8" fill="url(#scallop)"/>
    <rect class="scallop-edge" x="0" y="449" width="1200" height="8" fill="url(#scallop)"/>

    <line class="panel-divider" x1="400" y1="112" x2="400" y2="449"/>
    <line class="panel-divider" x1="800" y1="112" x2="800" y2="449"/>

    <rect class="figure-slot" x="158" y="266" width="44" height="162" rx="6" role="img" aria-label="Silhouette of a woman standing in the letter I"/>

    <g id="headline">
      <text class="headline-name" x="42" y="207" font-size="104" textLength="345" lengthAdjust="spacing">RINA’S</text>
      <text class="headline-line" x="40" y="250" font-size="42" textLength="350" lengthAdjust="spacing">Last Change to</text>
      <text class="headline-line" x="414" y="250" font-size="42" textLength="353" lengthAdjust="spacing">Celebrate Being</text>
      <text class="headline-word" x="42" y="428" font-size="232" textLength="741" lengthAdjust="spacing">SINGLE</text>
    </g>
  </svg>

  <dl class="details">
    <dt>Who</dt>
    <dd>RINA</dd>
    <dt>What</dt>
    <dd>Bachelorette Party</dd>
    <dt>Where</dt>
    <dd>TOLO Boat<br>Dubai Coral Quay Sailing Club</dd>
    <dt>When</dt>
    <dd>7th of February 2013</dd>
  </dl>
</main>
</body>
</html>
```